Veltiwell- Comprehensive quality healthcare delivered at your door.

I am looking for brochures to help promote my business. My business name is Veltiwel (see attachment and logo). This is a new health delivery system designed to provide high quality care to elderly in their communities or at home.

See attachements. The logo is already designed.

As far as services provided (see attachment)

Target Market(s)

Elderly patients

Industry/Entity Type

Business

Font styles to use
Serif

Colors

Designer to choose colors to be used in the design.

```html
<!DOCTYPE html>
<html lang="en">
<head>
<meta charset="utf-8">
<title>Veltiwel Tri-fold Brochure</title>
<link rel="stylesheet" href="https://fonts.googleapis.com/css2?family=Marcellus&family=Lato:wght@400;700&display=swap">
<style>
  :root{
    --green:#5b7018;
    --green-dark:#2f3f0a;
    --orange:#f39a12;
    --paper:#ffffff;
    --ink:#222222;
    --stage:#e4e4e4;
  }
  html,body{margin:0;padding:0;width:1200px;height:920px;overflow:hidden;background:var(--stage);}
  .brochure{position:absolute;left:30px;top:20px;width:1140px;height:880px;background:var(--paper);overflow:hidden;box-shadow:0 6px 18px rgba(0,0,0,.18);}
  .brochure-art{position:absolute;inset:0;}
  .fold{position:absolute;top:0;bottom:0;width:1px;background:rgba(0,0,0,.06);}
  .fold--one{left:380px}.fold--two{left:760px}
  .intro{position:absolute;left:60px;top:58px;width:275px;font-family:"Lato",sans-serif;font-size:11.5px;line-height:1.45;color:var(--ink);}
  .intro__title{font-family:"Marcellus",serif;font-size:15px;letter-spacing:.5px;color:var(--green-dark);margin:0 0 16px;}
  .intro p{margin:0 0 14px;text-align:justify;}
  .contact{position:absolute;left:296px;top:605px;font-family:"Lato",sans-serif;font-size:12.5px;color:var(--ink);}
  .contact__title{font-weight:700;font-size:15px;text-decoration:underline;margin:0 0 10px;color:var(--ink);}
  .contact__list{list-style:none;margin:0;padding:0;}
  .contact__item{display:flex;align-items:flex-start;gap:8px;margin-bottom:9px;line-height:1.3;}
  .contact__icon{flex:none;width:18px;height:18px;}
  .brand{position:absolute;left:760px;top:140px;width:380px;text-align:center;}
  .brand__mark{display:block;margin:0 auto 10px;width:62px;height:62px;border-radius:50%;background:var(--orange);}
  .brand__name{font-family:"Marcellus",serif;font-size:32px;letter-spacing:2px;color:var(--green-dark);margin:0;}
  .tagline{position:absolute;left:800px;top:712px;margin:0;font-family:"Marcellus",serif;font-weight:400;color:#fff;line-height:1;}
  .tagline__lead{display:block;font-size:36px;padding-left:22px;}
  .tagline__main{display:block;font-size:40px;letter-spacing:1px;margin-top:4px;}
</style>
</head>
<body>
<main class="brochure">
  <svg class="brochure-art" width="1140" height="880" viewBox="0 0 1140 880" xmlns="http://www.w3.org/2000/svg">
    <defs>
      <linearGradient id="fadedPhoto" x1="0" y1="0" x2="0" y2="1">
        <stop offset="0" stop-color="#d9d9d9"/>
        <stop offset=".55" stop-color="#c2c2c2"/>
        <stop offset="1" stop-color="#ffffff"/>
      </linearGradient>
      <linearGradient id="couplePhoto" x1="0" y1="0" x2="1" y2="1">
        <stop offset="0" stop-color="#eceeea"/>
        <stop offset=".5" stop-color="#a79f8e"/>
        <stop offset="1" stop-color="#4e5660"/>
      </linearGradient>
      <linearGradient id="groupPhoto" x1="0" y1="0" x2="1" y2="1">
        <stop offset="0" stop-color="#dfe6ea"/>
        <stop offset=".5" stop-color="#d8c2ae"/>
        <stop offset="1" stop-color="#9b8e80"/>
      </linearGradient>
    </defs>

    <g role="img" aria-label="Faded black and white photo of an older couple enjoying a walk outdoors">
      <rect x="380" y="0" width="380" height="620" fill="url(#fadedPhoto)"/>
    </g>

    <path class="wave wave--green" fill="var(--green)" d="M0,280 C220,235 450,250 540,330 C620,400 660,560 740,640 C800,695 900,705 1000,700 C1070,696 1110,682 1140,665 L1140,880 L0,880 Z"/>
    <path class="wave wave--orange" fill="var(--orange)" d="M0,305 C210,268 400,290 480,370 C570,460 600,700 660,880 L0,880 Z"/>
    <path class="wave wave--orange" fill="var(--orange)" d="M760,880 C900,872 1050,852 1140,832 L1140,880 Z"/>

    <g role="img" aria-label="Photo of a smiling older couple walking hand in hand outdoors">
      <circle cx="20" cy="570" r="248" fill="var(--green-dark)"/>
      <circle cx="20" cy="570" r="240" fill="url(#couplePhoto)"/>
    </g>

    <g role="img" aria-label="Photo of a cheerful group of older friends gathered together">
      <circle cx="985" cy="480" r="193" fill="var(--green-dark)"/>
      <circle cx="985" cy="480" r="185" fill="url(#groupPhoto)"/>
    </g>
  </svg>

  <div class="fold fold--one"></div>
  <div class="fold fold--two"></div>

  <section class="intro">
    <h2 class="intro__title">STAY HOME</h2>
    <p>Veltiwel offers home and Community Based Services for adults who wish to continue to live independently in the comfort of their communities.</p>
    <p>We provide on site services and deliver high quality health care at your door. Our experienced physicians coordinate care with our certified nurse practitioners and provide chronic care management, physical therapy, rehabilitation and medications management.</p>
  </section>

  <section class="contact">
    <h3 class="contact__title">Contact Us</h3>
    <ul class="contact__list">
      <li class="contact__item">
        <svg class="contact__icon" viewBox="0 0 18 18"><circle cx="9" cy="9" r="9" fill="#777"/><path d="M6 4.5l2 2-1 1.2c.6 1.3 1.5 2.2 2.8 2.8l1.2-1 2 2-1.3 1.5C8.5 12.5 5.5 9.5 4.5 5.8z" fill="#fff"/></svg>
        <span>555-014-2290</span>
      </li>
      <li class="contact__item">
        <svg class="contact__icon" viewBox="0 0 18 18"><circle cx="9" cy="9" r="9" fill="#777"/><circle cx="9" cy="9" r="5" fill="none" stroke="#fff" stroke-width="1.2"/><path d="M4 9h10M9 4c-2 3-2 7 0 10M9 4c2 3 2 7 0 10" fill="none" stroke="#fff" stroke-width="1"/></svg>
        <span>www.veltiwel-care.com</span>
      </li>
      <li class="contact__item">
        <svg class="contact__icon" viewBox="0 0 18 18"><circle cx="9" cy="9" r="9" fill="#777"/><rect x="4.5" y="5.5" width="9" height="7" fill="none" stroke="#fff" stroke-width="1.2"/><path d="M4.5 5.5L9 9.5l4.5-4" fill="none" stroke="#fff" stroke-width="1.2"/></svg>
        <span>hello@veltiwel-care.com</span>
      </li>
      <li class="contact__item">
        <svg class="contact__icon" viewBox="0 0 18 18"><circle cx="9" cy="9" r="9" fill="#777"/><path d="M9 3.8a3.6 3.6 0 0 0-3.6 3.6C5.4 10 9 14.2 9 14.2s3.6-4.2 3.6-6.8A3.6 3.6 0 0 0 9 3.8z" fill="#fff"/><circle cx="9" cy="7.4" r="1.3" fill="#777"/></svg>
        <span>48 Linden Ave.<br>Harbor Vale, FL 32911</span>
      </li>
    </ul>
  </section>

  <header class="brand">
    <span class="brand__mark"></span>
    <h1 class="brand__name">VELTIWEL</h1>
  </header>

  <h2 class="tagline">
    <span class="tagline__lead">Committed to</span>
    <span class="tagline__main">COMMUNITIES</span>
  </h2>
</main>
</body>
</html>
```